Law Firm Web Design Project

I need a website design for my law firm. I have attached to this description the URL of a website I liked with a description of the elements of that website that appeal to me.

I am also attaching my law firm's logo, so you can review that design when you create the website design.

Reference Site: www.harborfamilycounselpros.com

What we like about this site:
• The different layers
• Subtle designs, textures, curves
• 3 dimensional
• Floating effect
• Simple logo that stands out (we are providing logo)
• Prominent phone number
• Location of Areas of Practice
oDivorce, Legal Separation, Paternity, Spousal Maintenance, Child Custody, Child Support, Protective Orders, Community Property, Business Evaluations
• The limited amount of links across the top
o Home, Meet Our Attorney, FAQ, Contact Us
• Request A Consultation click through
• Right side bar with the moving icons
• Badges

Other Tips:
• We don’t want the website to be dark. The logo can standout and the website can have its own colors and flow.
• We would like there to be a “call to action” or way to get in touch on every page and every page view
• We would like a place for credit card icons at the bottom of the page
• Strong, yet elegant
• Finally, just use the website provided as a guide. Explore different colors, textures, shapes, shadows etc.
Updates

I would prefer the website have colors that are complementary to my logo and that are strong and elegant.  I like black, gold, amber, and tan colors.  Black should be used sparingly as an accent only, since I don't want the website to be too dark.

Please review the website I provided as an example in my project description.  I really like the three dimensional aspects of that website (web page floating on top of a background and the logo in the upper left floating on top of the web page).  I also like the use of "swirling" on the background and the webpage.  I hope this additional information is helpful.

Requirements
Must have
• I need a place to insert "client testimonials", a place to insert four logos of awards the law firm has received, a place for people to fill out a form to contact the law firm via email, and a place for people to click to review articles I have written.

```html
<!DOCTYPE html>
<html lang="en">
<head>
<meta charset="utf-8">
<title>Whitmore Law</title>
<link rel="stylesheet" href="https://fonts.googleapis.com/css2?family=Ubuntu:ital,wght@0,400;0,500;1,400&family=PT+Sans:ital,wght@0,400;0,700;1,400&display=swap">
<style>
:root{
  --backdrop:#e8d3b2;
  --page:#f8f3ec;
  --band:#e6d8c5;
  --sidebar:#e6d8c4;
  --navy:#1f3c64;
  --text:#555049;
  --muted:#6f675d;
  --gold:#a88a4a;
  --dark:#2e2e2e;
  --footer:#bcab96;
  --badge:#a8a29a;
}
*{margin:0;padding:0;box-sizing:border-box}
html,body{width:1100px;height:1200px;overflow:hidden}
body{background:var(--backdrop);font-family:"PT Sans",sans-serif;color:var(--text);position:relative}
.page{position:absolute;left:61px;top:0;width:978px;height:1200px;background:var(--page);box-shadow:0 0 6px rgba(120,90,50,.25)}
.abs{position:absolute}
.brand{left:10px;top:12px;display:flex;align-items:center;gap:14px}
.brand-mark{width:58px;height:58px;background:var(--dark)}
.brand-name{font-family:"Ubuntu",sans-serif;font-weight:400;font-size:34px;color:var(--gold)}
.phone-tab{left:731px;top:0;width:247px;height:46px;background:var(--band);border-bottom-left-radius:24px;display:flex;align-items:center;padding-left:26px;gap:8px;font-family:"Ubuntu",sans-serif;font-size:16px;color:#444}
.nav-band{left:0;top:77px;width:912px;height:51px;background:linear-gradient(90deg,rgba(230,216,197,0) 5%,var(--band) 55%);border-top-right-radius:30px}
.nav{right:21px;top:18px;display:flex;gap:22px;font-family:"Ubuntu",sans-serif;font-size:14px;color:#333;list-style:none}
.nav li.active{color:var(--navy)}
.nav .sep{color:#333}
.header-rule{left:0;top:128px;width:978px;height:5px;background:#eee3d5}
.hero-photo{left:0;top:133px;width:978px;height:309px;background:linear-gradient(90deg,#f4f0ea 0%,#ede6dc 35%,#c9a88a 62%,#e9dfd2 85%,#f2ede6 100%)}
.hero-title{left:47px;top:235px;font-family:"Ubuntu",sans-serif;font-size:25px;color:var(--navy)}
.hero-text{left:48px;top:278px;width:258px;font-size:13px;line-height:18px;text-align:justify;color:#333}
.dots{left:108px;top:390px;display:flex;gap:17px;align-items:center}
.dots span{width:14px;height:14px;border-radius:50%;background:#6b6b6b}
.dots span.on{width:18px;height:18px;background:#333;border:3px solid #aaa}
.sidebar-shape{left:0;top:444px}
h2{font-family:"Ubuntu",sans-serif;font-weight:400;font-size:18px;color:var(--navy)}
.dotted{border-bottom:2px dotted #9b8f80;width:211px}
.quote{font-style:italic;font-size:13px;line-height:18px;width:214px;color:#4a4540}
.author{font-weight:700;font-size:13px;color:#4a4540}
.cta{left:9px;top:701px;width:213px;height:88px;border-radius:7px;background:linear-gradient(#6a6a6a,#2e2e2e);box-shadow:0 2px 4px rgba(0,0,0,.3)}
.cta-title{position:absolute;right:16px;top:14px;font-family:"Ubuntu",sans-serif;font-style:italic;font-size:21px;color:#fff}
.cta-link{position:absolute;right:17px;top:47px;font-size:11px;color:#eee;text-decoration:underline}
.cta-icon{position:absolute;left:12px;top:30px}
.contact-text{font-size:13px;line-height:20px;color:#4a4540}
.social{left:21px;top:1033px;display:flex;gap:10px}
.social span{width:25px;height:24px;background:#3a3a3a;color:#fff;font-size:5.5px;display:flex;align-items:center;justify-content:center;border-radius:2px}
.main-text{font-size:12.5px;line-height:20px;text-align:justify;color:var(--text)}
.view-more{right:15px;top:651px;font-family:"Ubuntu",sans-serif;font-size:14px;color:var(--navy)}
.rule{left:272px;top:686px;width:696px;height:1px;background:#b9ae9f}
.practice{list-style:none;font-size:13px;line-height:24px;color:#4a4540}
.practice li{padding-left:15px;position:relative}
.practice li::before{content:"";position:absolute;left:0;top:8px;border-left:5px solid #555;border-top:4px solid transparent;border-bottom:4px solid transparent}
.certs{left:271px;top:999px;width:697px;height:85px;background:#ebe0d1;border-radius:8px}
.certs-label{position:absolute;left:0;top:20px;width:155px;text-align:center;font-family:"Ubuntu",sans-serif;font-size:17px;line-height:22px;color:#6a6258}
.badge{position:absolute;background:var(--badge);border-radius:4px;opacity:.8}
.footer{left:0;top:1101px;width:978px;height:99px;background:var(--footer)}
.footer-links{position:absolute;left:12px;top:24px;font-size:12px;color:#3b3630;word-spacing:2px}
.copy{position:absolute;left:12px;top:58px;font-size:12px;color:#3b3630}
.cards{position:absolute;right:10px;top:41px;display:flex;gap:8px}
.cards span{width:29px;height:20px;background:#f4f1ec;border-radius:3px;font-size:6px;color:#333;display:flex;align-items:center;justify-content:center}
</style>
</head>
<body>
<div class="page">
  <header>
    <div class="abs brand"><span class="brand-mark"></span><span class="brand-name">Whitmore Law</span></div>
    <div class="abs phone-tab">
      <svg width="16" height="20" viewBox="0 0 16 20" aria-hidden="true"><path d="M3 1l4 0 1 5-3 2c1 3 2 5 4 7l3-2 4 3-1 3c-1 1-3 1-5 0C5 16 2 11 1 6 1 3 2 1 3 1z" fill="#555"/></svg>
      <span>Call Us : 555 201 7730</span>
    </div>
    <div class="abs nav-band">
      <ul class="abs nav">
        <li class="active">Home</li><li class="sep">|</li><li>Meet Our Attorney</li><li class="sep">|</li><li>FAQ</li><li class="sep">|</li><li>Contact Us</li>
      </ul>
    </div>
    <div class="abs header-rule"></div>
  </header>

  <section>
    <div class="abs hero-photo" role="img" aria-label="Photograph of a young woman resting her head on an open book"></div>
    <h1 class="abs hero-title" style="font-weight:400">Excepteur sint occaecat</h1>
    <p class="abs hero-text">Quis autem vel eum iure reprehenderit qui in ea voluptate velit esse quam nihil lemit molestiae consequatu</p>
    <div class="abs dots"><span class="on"></span><span></span><span></span><span></span><span></span></div>
  </section>

  <aside>
    <svg class="abs sidebar-shape" width="262" height="657" viewBox="0 0 262 657" aria-hidden="true">
      <path d="M0 0H232C262 20 262 60 259 110V560C259 610 255 630 248 657H0Z" fill="var(--sidebar)"/>
    </svg>
    <h2 class="abs" style="left:10px;top:459px">Clients Testimonials</h2>
    <div class="abs dotted" style="left:10px;top:489px"></div>
    <p class="abs quote" style="left:10px;top:503px">“ Neque porro quisquam &nbsp;qui dolorem ipsum quia dolor sit amet, consectetur, adipisci velit “</p>
    <p class="abs author" style="left:125px;top:561px">- voluptate velit</p>
    <p class="abs quote" style="left:10px;top:604px">“ Neque porro quisquam &nbsp;qui dolorem ipsum quia dolor sit amet, consectetur, adipisci velit “</p>
    <p class="abs author" style="left:125px;top:662px">- voluptate velit</p>
    <div class="abs cta">
      <svg class="cta-icon" width="52" height="46" viewBox="0 0 52 46" aria-hidden="true">
        <ellipse cx="26" cy="20" rx="25" ry="19" fill="#dfe6ee"/>
        <path d="M10 34l-4 10 12-7z" fill="#dfe6ee"/>
        <path d="M16 10h6l2 6-4 3c2 4 4 6 8 8l3-4 6 2v6c-3 2-8 2-13-1-6-4-9-9-10-15 0-3 1-5 2-5z" fill="#2c5a8a"/>
      </svg>
      <div class="cta-title">Call to Auction</div>
      <div class="cta-link">Click Here for contact us</div>
    </div>
    <h2 class="abs" style="left:10px;top:812px">Contact us</h2>
    <div class="abs dotted" style="left:10px;top:842px"></div>
    <p class="abs contact-text" style="left:21px;top:855px">Neque porro quisquam,<br>qui dolorem ipsum,<br>quia dolor sit amet,<br>consectetur.</p>
    <p class="abs contact-text" style="left:21px;top:941px;font-size:12.5px;line-height:18px">Phone : 555 201 7730<br>&nbsp;&nbsp;&nbsp;&nbsp;&nbsp;Fax : 555 201 7731<br>E-mail : info@whitmorelaw.com</p>
    <p class="abs contact-text" style="left:21px;top:1003px">Connect with us :</p>
    <div class="abs social"><span>Circle</span><span>Chirp</span><span>Worklink</span><span>Feed</span><span>Journal</span></div>
  </aside>

  <main>
    <h2 class="abs" style="left:275px;top:460px">Welcome to our site</h2>
    <p class="abs main-text" style="left:276px;top:502px;width:686px">Sed ut perspiciatis unde omnis iste natus error sit voluptatem accusantium doloremque laudantium, totam rem aperiam, eaque ipsa quae ab illo inventore veritatis et quasi architecto beatae vitae dicta sunt explicabo. Nemo enim ipsam voluptatem quia voluptas sit aspernatur aut odit aut fugit, sed quia consequuntur magni dolores eos qui ratione voluptatem sequi nesciunt. Neque porro quisquam est, qui dolorem ipsum quia dolor sit amet, consectetur, adipisci velit, sed quia non numquam eius modi tempora incidunt ut labore et dolore magnam aliquam quaerat voluptatem. Ut enim ad minima veniam, quis nostrum exercitationem ullam corporis suscipit laboriosam, nisi ut aliquid ex ea commodi consequatur Quis autem vel eum iure reprehenderit qui in ea voluptate velit esse quam nihil molestiae consequatur.</p>
    <div class="abs view-more">View more</div>
    <div class="abs rule"></div>
    <h2 class="abs" style="left:275px;top:704px">Areas of Practice</h2>
    <p class="abs main-text" style="left:276px;top:746px;width:686px">Voluptatem sequi nesciunt. Neque porro quisquam est, qui dolorem ipsum quia dolor sit amet, consectetur, adipisci velit, sed quia non numquam eius modi tempora incidunt ut labore et dolore magnam aliquam quaerat voluptatem. Ut enim ad minima veniam, quis nostrum exercitationem ullam corporis suscipit laboriosam.</p>
    <ul class="abs practice" style="left:305px;top:817px"><li>Family Law</li><li>Divorce</li><li>Alimony</li><li>Child Custody</li><li>Child Support</li><li>Collaborative Divorce</li><li>Contested Divorce</li></ul>
    <ul class="abs practice" style="left:486px;top:817px"><li>Division of Assets</li><li>Domestic Violence</li><li>Family/Relative Adoption</li><li>Fathers’ Rights</li><li>Grandparents’ Rights</li><li>Guardianship</li><li>Legal Separation</li></ul>
    <ul class="abs practice" style="left:687px;top:817px"><li>Mediation</li><li>Modification of Spousal Support</li><li>Mothers’ Rights</li><li>Palimony</li><li>Parental Alienation</li><li>Paternity</li><li>Prenuptial Agreements</li></ul>
    <div class="abs certs">
      <div class="certs-label">Our<br>Certifications</div>
      <div class="badge" style="left:183px;top:12px;width:90px;height:62px"></div>
      <div class="badge" style="left:309px;top:12px;width:142px;height:62px"></div>
      <div class="badge" style="left:497px;top:10px;width:181px;height:64px"></div>
    </div>
  </main>

  <footer class="abs footer">
    <div class="footer-links">Home &nbsp;| &nbsp;Meet Our Attorney &nbsp;| &nbsp;FAQ &nbsp;| &nbsp;Contact Us &nbsp;| &nbsp;Sitemap</div>
    <div class="copy">Copyright © 2012 www.whitmorelaw.com &nbsp;&nbsp;All rights reserved</div>
    <div class="cards"><span>PayEase</span><span>Cardo</span><span>Orbis</span><span>Quickpay</span><span>Vanta</span></div>
  </footer>
</div>
</body>
</html>
```